Tech Company Letterhead/Business Cards/Envelopes

We would like a new stationary design for a technology company that develops full turnkey solutions for governments related to Data, Identity Tracking, Fingerprinting, Passport Control, and Border Protection Systems.

We would like the stationary designs to include:

Letter Head
Business Cards
Envelopes

Target Market(s)

Corporate

Industry/Entity Type

Business

Contact Information for Business Card

Details to be shared with the winner.

Font styles to use
Serif
Sans Serif

Colors
e4daeb
85abd2
3176b5
0355a3
0692cd

```html
<!DOCTYPE html>
<html lang="en">
<head>
<meta charset="utf-8">
<title>Veridon Business Cards</title>
<link href="https://fonts.googleapis.com/css2?family=Questrial&display=swap" rel="stylesheet">
<style>
  :root {
    --page: #eceef1;
    --brand-blue: #1f6fbf;
    --front-light: #4a94d6;
    --front-dark: #2d74bd;
    --ink-gray: #4a4a4a;
    --band-gray: #5f6062;
    --card-white: #ffffff;
  }
  * { margin: 0; padding: 0; box-sizing: border-box; }
  html, body { width: 1200px; height: 900px; overflow: hidden; }
  body {
    background: var(--page);
    font-family: "Questrial", "Century Gothic", sans-serif;
    position: relative;
  }
  .card {
    position: absolute;
    left: 320px;
    width: 560px;
    height: 320px;
    border-radius: 20px;
    overflow: hidden;
    box-shadow: 0 6px 18px rgba(0,0,0,0.12);
  }
  .card-front {
    top: 90px;
    background: linear-gradient(160deg, var(--front-light) 0%, var(--front-dark) 100%);
  }
  .card-front .brand-name {
    position: absolute;
    right: 48px;
    bottom: 70px;
    color: var(--card-white);
    font-size: 50px;
    letter-spacing: 3px;
  }
  .card-back {
    top: 490px;
    background: var(--card-white);
  }
  .card-back .brand-name {
    position: absolute;
    right: 34px;
    top: 40px;
    color: var(--brand-blue);
    font-size: 54px;
    letter-spacing: 3px;
  }
  .divider {
    position: absolute;
    left: 178px;
    right: 28px;
    top: 168px;
    height: 2px;
    background: var(--brand-blue);
  }
  .person {
    position: absolute;
    left: 32px;
    top: 158px;
  }
  .person-name {
    color: var(--brand-blue);
    font-size: 16px;
    letter-spacing: 0.5px;
  }
  .person-title {
    color: var(--ink-gray);
    font-size: 15px;
    margin-left: 10px;
    margin-top: 2px;
  }
  .contacts {
    position: absolute;
    left: 40px;
    top: 208px;
    list-style: none;
    color: var(--ink-gray);
    font-size: 16px;
    line-height: 21px;
  }
  .contacts li { display: flex; align-items: center; gap: 8px; }
  .contacts svg { width: 12px; height: 12px; flex: none; }
  .address {
    position: absolute;
    right: 36px;
    top: 228px;
    text-align: right;
    color: var(--ink-gray);
    font-size: 14px;
    line-height: 18px;
  }
  .bottom-bands {
    position: absolute;
    left: 0;
    bottom: 0;
    width: 560px;
    height: 44px;
  }
</style>
</head>
<body>
  <section class="card card-front">
    <div class="brand-name">VERIDON</div>
  </section>

  <section class="card card-back">
    <div class="brand-name">VERIDON</div>
    <div class="divider"></div>
    <div class="person">
      <div class="person-name">EMPLOYEE NAME</div>
      <div class="person-title">Title</div>
    </div>
    <ul class="contacts">
      <li>
        <svg viewBox="0 0 12 12"><rect x="0" y="0" width="12" height="12" rx="2" fill="var(--brand-blue)"/><path d="M3.5 2.5 L5 4 L4.2 5 Q5 7 7 7.8 L8 7 L9.5 8.5 L8.5 9.6 Q4 9 2.4 3.5 Z" fill="#fff"/></svg>
        555.014.2386
      </li>
      <li>
        <svg viewBox="0 0 12 12"><rect x="3" y="0.5" width="6" height="3" fill="var(--brand-blue)"/><rect x="0.5" y="4" width="11" height="5" rx="1" fill="var(--brand-blue)"/><rect x="3" y="7.5" width="6" height="4" fill="var(--brand-blue)"/><rect x="4" y="8.5" width="4" height="2" fill="#fff"/></svg>
        555.014.2390
      </li>
      <li>
        <svg viewBox="0 0 12 12"><rect x="0.5" y="2" width="11" height="8" fill="var(--brand-blue)"/><path d="M0.5 2 L6 6.5 L11.5 2" fill="none" stroke="#fff" stroke-width="1"/></svg>
        info@website.com
      </li>
      <li>
        <svg viewBox="0 0 12 12"><circle cx="6" cy="6" r="5.2" fill="none" stroke="var(--brand-blue)" stroke-width="1"/><ellipse cx="6" cy="6" rx="2.2" ry="5.2" fill="none" stroke="var(--brand-blue)" stroke-width="0.9"/><line x1="0.8" y1="6" x2="11.2" y2="6" stroke="var(--brand-blue)" stroke-width="0.9"/></svg>
        www.website.com
      </li>
    </ul>
    <div class="address">2240 Harbor Way Suite 210,<br>Oregon USA 97204</div>
    <svg class="bottom-bands" viewBox="0 0 560 44" preserveAspectRatio="none">
      <rect x="0" y="32" width="356" height="12" fill="var(--brand-blue)"/>
      <polygon points="352,44 362,10 560,10 560,44" fill="var(--band-gray)"/>
    </svg>
  </section>
</body>
</html>
```